Business Card Design

I need a business card for my rental business. The business is named:
Hire a Vorlatrike Brenmoor
www.hireavorlatrikebrenmoor.example
(555) 014-2937
This will be a business card that I will leave at other businesses as advertisement so it needs to have the name, website, and phone number.
Please feel free to be creative. This is a new business so I have no designs.
Thank you very much for your time and I look forward to receiving your designs
Target Market(s)
Local rental customers
Industry/Entity Type
Business
Contact Information for Business Card
Please check out my website:
Other font styles liked:
- anything creative
Colors
Designer to choose colors to be used in the design.
Requirements
Must have
- Business name, phone, website. Rentals available hourly or daily. Book online

```html
<!DOCTYPE html>
<html lang="en">
<head>
<meta charset="utf-8">
<title>Hire a Vorlatrike Brenmoor – Business Card</title>
<link rel="stylesheet" href="https://fonts.googleapis.com/css2?family=Arimo:wght@400&family=Crimson+Text:wght@400&family=Poppins:wght@600&display=swap">
<style>
  :root {
    --page: #ffffff;
    --card: #dcdcdc;
    --sheen-light: #ffffff;
    --sheen-shade: #d4d4d4;
    --ink: #231f20;
    --ink-inverse: #ffffff;
    --icon-fill: #c9c9c9;
  }
  * { margin: 0; padding: 0; box-sizing: border-box; }
  html, body {
    width: 1200px;
    height: 848px;
    overflow: hidden;
    background: var(--page);
  }
  .business-card {
    position: absolute;
    left: 289px;
    top: 227px;
    width: 616px;
    height: 387px;
    background: var(--card);
    overflow: hidden;
  }
  .card-sheen {
    position: absolute;
    inset: 0;
  }
  .brand-mark {
    position: absolute;
    left: 24px;
    top: 72px;
    width: 58px;
    height: 58px;
    background: var(--ink);
  }
  .brand-name {
    position: absolute;
    left: 94px;
    top: 60px;
    color: var(--ink);
    font-family: "Arimo", Arial, sans-serif;
    font-weight: 400;
  }
  .brand-name .brand-lead {
    display: block;
    font-size: 78px;
    line-height: 76px;
    letter-spacing: -1px;
  }
  .brand-name .brand-rest {
    display: block;
    font-size: 26px;
    line-height: 30px;
    margin-left: 2px;
  }
  .service-note {
    position: absolute;
    right: 20px;
    top: 128px;
    color: var(--ink);
    font-family: "Arimo", Arial, sans-serif;
    font-size: 16px;
    line-height: 21px;
    text-align: right;
  }
  .phone-band {
    position: absolute;
    left: 0;
    top: 241px;
    width: 616px;
    height: 66px;
    background: var(--ink);
  }
  .phone-icon {
    position: absolute;
    left: 20px;
    top: 227px;
    width: 53px;
    height: 101px;
  }
  .phone-number {
    position: absolute;
    left: 96px;
    top: 232px;
    color: var(--ink-inverse);
    font-family: "Crimson Text", "Book Antiqua", serif;
    font-size: 72px;
    line-height: 80px;
    letter-spacing: 3.5px;
    white-space: nowrap;
  }
  .website-icon {
    position: absolute;
    left: 13px;
    top: 339px;
    width: 33px;
    height: 33px;
  }
  .website {
    position: absolute;
    left: 56px;
    top: 338px;
    color: var(--ink);
    font-family: "Poppins", "Century Gothic", sans-serif;
    font-weight: 600;
    font-size: 24px;
    line-height: 34px;
    white-space: nowrap;
  }
</style>
</head>
<body>
  <div class="business-card">
    <svg class="card-sheen" width="616" height="387" viewBox="0 0 616 387" aria-hidden="true">
      <defs>
        <linearGradient id="sheen-gradient" x1="0" y1="0" x2="1" y2="0">
          <stop offset="0" stop-color="var(--sheen-shade)"/>
          <stop offset="0.55" stop-color="var(--sheen-light)"/>
          <stop offset="1" stop-color="var(--sheen-light)"/>
        </linearGradient>
      </defs>
      <ellipse cx="220" cy="80" rx="210" ry="130" fill="url(#sheen-gradient)"/>
    </svg>

    <div class="brand-mark"></div>
    <h1 class="brand-name">
      <span class="brand-lead">Hire</span>
      <span class="brand-rest">a Vorlatrike Brenmoor</span>
    </h1>

    <p class="service-note">Rentals available<br>hourly or daily.<br>Book online</p>

    <div class="phone-band"></div>
    <svg class="phone-icon" viewBox="0 0 53 101" aria-hidden="true">
      <rect x="3" y="3" width="47" height="95" rx="3" fill="var(--icon-fill)" stroke="var(--ink)" stroke-width="5"/>
      <rect x="11" y="14" width="31" height="70" fill="var(--card)" stroke="var(--ink)" stroke-width="2"/>
    </svg>
    <p class="phone-number">(555) 014-2937</p>

    <svg class="website-icon" viewBox="0 0 33 33" aria-hidden="true">
      <g fill="none" stroke="var(--ink)" stroke-width="2.6">
        <circle cx="16.5" cy="16.5" r="14"/>
        <ellipse cx="16.5" cy="16.5" rx="6" ry="14"/>
        <line x1="2.5" y1="16.5" x2="30.5" y2="16.5"/>
        <line x1="16.5" y1="2.5" x2="16.5" y2="30.5"/>
      </g>
    </svg>
    <p class="website">www.hireavorlatrikebrenmoor.example</p>
  </div>
</body>
</html>
```